Business Card Design Project

I need a new business card design for my building/development company: Kestrel Ridge Builders.

We specialise in small sub-divisions, multi-story developments and new house builds.
We handle the whole process from concept stage right throught to a fully developed property.
Updates

Target Market(s)

people looking to develop their property and need help. New property buyers

Industry/Entity Type

House

Requirements
Must have
• My logo on both sides:
Side 1: Logo taking up whole side as per old card but with a color/style change.

Side 2: Contact page: include logo but the rest just surprise me!

All contact details will be: (and need to be changable for each employee) I'll inform you of specifics before printing.

Name Surname
Position ie. Managing director
M: insert mobile
E: insert email
P.O. Box 518, Ashwell, Vic, 3094
www.kestrelridgebuilders.com.au

Nice to have
• Colors i'd like: (not necessarily all but this is the basic idea)

Black, blue, grey, silver, white

```html
<!DOCTYPE html>
<html lang="en">
<head>
<meta charset="utf-8">
<title>Kestrel Ridge Builders – Business Cards</title>
<link rel="stylesheet" href="https://fonts.googleapis.com/css2?family=Open+Sans:wght@400;600;700&display=swap">
<style>
  :root {
    --page-bg: #e9ebee;
    --brand-blue: #1a8ccf;
    --brand-blue-deep: #0a5f93;
    --brand-blue-light: #3aa8e4;
    --band-light: #6fbde9;
    --card-white: #f7f7f7;
    --card-grey: #dcdcdc;
    --silver: #b9bcbf;
    --ink: #1e1e1e;
    --ink-soft: #333;
    --white: #ffffff;
  }
  * { box-sizing: border-box; margin: 0; padding: 0; }
  html, body {
    width: 1200px; height: 900px; overflow: hidden;
    background: var(--page-bg);
    font-family: "Open Sans", Arial, sans-serif;
  }
  .card-set { position: relative; width: 1200px; height: 900px; }
  .card {
    position: absolute; left: 280px;
    width: 640px; height: 366px;
    border-radius: 22px; overflow: hidden;
    box-shadow: 0 6px 18px rgba(0,0,0,.18);
  }

  /* Front side */
  .card--front {
    top: 70px;
    background: radial-gradient(ellipse at 35% 40%, var(--brand-blue-light) 0%, var(--brand-blue) 45%, var(--brand-blue-deep) 100%);
    color: var(--white);
  }
  .front-brand {
    position: absolute; left: 0; right: 0; top: 120px;
    text-align: center;
  }
  .front-brand__name {
    font-size: 40px; font-weight: 700; letter-spacing: -0.5px; line-height: 1;
  }
  .front-brand__tagline {
    margin-top: 6px; font-size: 17px; font-weight: 600;
  }
  .front-web {
    position: absolute; left: 0; right: 0; bottom: 42px;
    text-align: center; font-size: 15px;
  }

  /* Back side */
  .card--back {
    top: 464px;
    background: linear-gradient(160deg, var(--card-white) 0%, var(--card-grey) 100%);
    color: var(--ink);
  }
  .back-brand { position: absolute; left: 40px; top: 44px; }
  .back-brand__name {
    font-size: 27px; font-weight: 700; color: var(--brand-blue); line-height: 1;
  }
  .back-brand__tagline { margin-top: 4px; font-size: 12px; color: var(--ink-soft); }
  .person { position: absolute; right: 60px; top: 84px; text-align: center; }
  .person__name { font-size: 22px; font-weight: 400; }
  .person__name strong { font-weight: 700; }
  .person__role { font-size: 14px; font-weight: 600; margin-top: 2px; }

  .contact-list {
    position: absolute; left: 38px; top: 128px; list-style: none;
    font-size: 14px;
  }
  .contact-list li { display: flex; align-items: center; height: 25px; }
  .contact-list .pair { display: flex; gap: 22px; }
  .contact-item { display: flex; align-items: center; gap: 10px; }
  .icon { width: 17px; height: 17px; flex: none; }

  .accent-band {
    position: absolute; left: 0; right: 0; bottom: 0; height: 106px;
    background: linear-gradient(180deg, var(--band-light) 0%, var(--brand-blue) 100%);
    border-top: 6px solid var(--silver);
  }
</style>
</head>
<body>
<main class="card-set">

  <section class="card card--front" aria-label="Business card front">
    <div class="front-brand">
      <div class="front-brand__name">Kestrel Ridge Builders</div>
      <div class="front-brand__tagline">renovation-construction-development</div>
    </div>
    <div class="front-web">www.kestrelridgebuilders.com.au</div>
  </section>

  <section class="card card--back" aria-label="Business card back">
    <div class="accent-band" role="img" aria-label="Decorative blue, silver and white wave band along the bottom of the card"></div>

    <div class="back-brand">
      <div class="back-brand__name">Kestrel Ridge Builders</div>
      <div class="back-brand__tagline">renovation-construction-development</div>
    </div>

    <div class="person">
      <div class="person__name"><strong>Daniel</strong> Harte</div>
      <div class="person__role">General Manager</div>
    </div>

    <ul class="contact-list">
      <li class="contact-item">
        <svg class="icon" viewBox="0 0 20 20"><circle cx="10" cy="10" r="10" fill="var(--brand-blue)"/><path d="M5 10.5 L10 6 L15 10.5 M6.5 9.5 V14.5 H13.5 V9.5" fill="none" stroke="#fff" stroke-width="1.6"/></svg>
        <span>P.O. Box 518, Ashwell, Vic, 3094</span>
      </li>
      <li class="pair">
        <span class="contact-item">
          <svg class="icon" viewBox="0 0 20 20"><circle cx="10" cy="10" r="10" fill="var(--brand-blue)"/><path d="M6 7 Q10 4 14 7 L13 9 L11 8.5 V10 H9 V8.5 L7 9 Z M6.5 11 H13.5 V14.5 H6.5 Z" fill="#fff"/></svg>
          <span>(07) 3512 4480</span>
        </span>
        <span class="contact-item">
          <svg class="icon" viewBox="0 0 20 20"><circle cx="10" cy="10" r="10" fill="var(--brand-blue)"/><rect x="7" y="4.5" width="6" height="11" rx="1" fill="#fff"/><rect x="8" y="6" width="4" height="6" fill="var(--brand-blue)"/></svg>
          <span>0412 765 309</span>
        </span>
      </li>
      <li class="contact-item">
        <svg class="icon" viewBox="0 0 20 20"><circle cx="10" cy="10" r="10" fill="var(--brand-blue)"/><rect x="5" y="6.5" width="10" height="7" fill="#fff"/><path d="M5 6.5 L10 10.5 L15 6.5" fill="none" stroke="var(--brand-blue)" stroke-width="1.2"/></svg>
        <span>sample@kestrelridgebuilders.com.au</span>
      </li>
      <li class="contact-item">
        <svg class="icon" viewBox="0 0 20 20"><circle cx="10" cy="10" r="10" fill="var(--brand-blue)"/><circle cx="10" cy="10" r="5" fill="none" stroke="#fff" stroke-width="1.3"/><path d="M5 10 H15 M10 5 V15" stroke="#fff" stroke-width="1.1"/></svg>
        <span>www.kestrelridgebuilders.com.au</span>
      </li>
    </ul>
  </section>

</main>
</body>
</html>
```